Bref créative
Business Cards, Letterhead, Envelopes, Fax Cover, Email Signature, Truck
Brindle Roofing Ltd.
I need double sided standard sized Business Card [3.5" x 2"]
Do not limit yourself to font used in logo
Professional
Tomasz Oduya
42 Fairwick Lane NE
Calgary AB T3M2R8
tomi@brindleroofing.example
www.brindleroofing.example
Open to different ideas. For example : just logo, web address etc
Photograph-1 of truck
Picture 2
Picture-3
Picture-4
Picture-5
Color scheme(s)to be used for Truck

```html
<!DOCTYPE html>
<html lang="en">
<head>
<meta charset="utf-8">
<title>Brindle Roofing Ltd. – Business Card</title>
<link rel="stylesheet" href="https://fonts.googleapis.com/css2?family=Open+Sans:wght@400;600;700&display=swap">
<style>
  :root {
    --backdrop: #e4e1dc;
    --card-white: #ffffff;
    --band-light: #cfcfcf;
    --band-dark: #8f8f8f;
    --back-light: #b9b9b9;
    --back-dark: #7a7a7a;
    --brand-green: #6a9a2a;
    --text-grey: #6b6b6b;
    --white: #ffffff;
  }
  * { margin: 0; padding: 0; box-sizing: border-box; }
  html, body { width: 1200px; height: 674px; overflow: hidden; }
  body {
    background: var(--backdrop);
    font-family: "Open Sans", Arial, sans-serif;
    position: relative;
  }
  .card {
    position: absolute;
    top: 224px;
    width: 396px;
    height: 226px;
    border-radius: 12px;
    overflow: hidden;
    box-shadow: 0 6px 16px rgba(0,0,0,0.25);
  }
  .card--front { left: 204px; background: var(--card-white); }
  .card--back {
    left: 604px;
    background: linear-gradient(135deg, var(--back-light) 0%, #a3a3a3 55%, var(--back-dark) 100%);
  }
  .front-band {
    position: absolute; left: 0; top: 0; width: 100%; height: 54px;
    background: linear-gradient(90deg, var(--band-dark) 0%, var(--band-light) 100%);
  }
  .front-sphere {
    position: absolute; left: 0; top: 0; width: 84px; height: 70px;
    background: radial-gradient(circle closest-side at 50% 50%, rgba(255,255,255,0.85), rgba(255,255,255,0.3) 60%, rgba(255,255,255,0) 100%);
  }
  .holder-name {
    position: absolute; left: 90px; top: 16px;
    color: var(--white); font-weight: 700; font-size: 15px; letter-spacing: 1px;
  }
  .brand {
    position: absolute; left: 24px; top: 88px;
    display: flex; align-items: center; gap: 8px;
  }
  .brand-dot { width: 22px; height: 22px; border-radius: 50%; background: var(--brand-green); }
  .brand-name {
    color: var(--brand-green); font-weight: 600; font-size: 25px; letter-spacing: -0.5px;
  }
  .contact {
    position: absolute; left: 90px; top: 150px;
    list-style: none; color: var(--text-grey); font-size: 8px; line-height: 17px;
  }
  .contact li { display: flex; align-items: center; gap: 5px; white-space: nowrap; }
  .contact svg { flex: none; }
  .contact .gap { margin-left: 8px; }
  .back-sphere {
    position: absolute; left: -20px; top: -10px; width: 250px; height: 230px;
    background: radial-gradient(circle closest-side at 50% 50%, rgba(255,255,255,0.8), rgba(255,255,255,0.3) 60%, rgba(255,255,255,0) 100%);
  }
  .back-web {
    position: absolute; right: 20px; bottom: 26px;
    color: var(--white); font-size: 12px;
  }
  .back-web b { font-weight: 700; }
</style>
</head>
<body>
  <section class="card card--front">
    <div class="front-band"></div>
    <div class="front-sphere" role="img" aria-label="Decorative dotted sphere graphic"></div>
    <h1 class="holder-name">TOMASZ ODUYA</h1>
    <div class="brand">
      <span class="brand-dot"></span>
      <span class="brand-name">brindleroofing Ltd.</span>
    </div>
    <ul class="contact">
      <li>
        <svg width="8" height="8" viewBox="0 0 10 10"><path d="M5 0a3.5 3.5 0 0 0-3.5 3.5C1.5 6 5 10 5 10s3.5-4 3.5-6.5A3.5 3.5 0 0 0 5 0z" fill="#6a9a2a"/></svg>
        42 Fairwick Lane NE Calgary AB T3M2R8
      </li>
      <li>
        <svg width="8" height="8" viewBox="0 0 10 10"><path d="M2 0h2l1 3-1.5 1a6 6 0 0 0 2.5 2.5L7 5l3 1v2a2 2 0 0 1-2 2A8 8 0 0 1 0 2a2 2 0 0 1 2-2z" fill="#6a9a2a"/></svg>
        4035550142
        <svg class="gap" width="8" height="8" viewBox="0 0 10 10"><rect x="2" y="0" width="6" height="10" rx="1" fill="#6a9a2a"/></svg>
        4035550143
        <svg class="gap" width="8" height="8" viewBox="0 0 10 10"><rect x="1" y="2" width="8" height="7" fill="#6a9a2a"/></svg>
        4035550144
      </li>
      <li>
        <svg width="8" height="8" viewBox="0 0 10 10"><rect x="0" y="2" width="10" height="7" fill="#6a9a2a"/><path d="M0 2l5 4 5-4" stroke="#fff" fill="none"/></svg>
        tomi@brindleroofing.example
        <svg class="gap" width="8" height="8" viewBox="0 0 10 10"><circle cx="5" cy="5" r="4.5" fill="#6a9a2a"/></svg>
        www.brindleroofing.example
      </li>
    </ul>
  </section>

  <section class="card card--back">
    <div class="back-sphere" role="img" aria-label="Decorative dotted sphere graphic"></div>
    <p class="back-web">www.<b>brindleroofing</b>.example</p>
  </section>
</body>
</html>
```